continuing medical education travel company. luxury, professional, quality service

PLEASE USE THE REVISED LOGO FOR ALL CARD DESIGNS, NO SNAKE HEAD

Target Market(s)

physicians

Industry/Entity Type

Travel Industry

Contact Information for Business Card

luxury quality, spot uv, foil, rounded corners

Colors
0255a3
3176b5
cfdeed
aaaaaa
5c5c5c

Requirements
Must have
• navy, platinum, possible holographic

```html
<!DOCTYPE html>
<html lang="en">
<head>
<meta charset="utf-8">
<title>Solace Travel – Business Card</title>
<link rel="stylesheet" href="https://fonts.googleapis.com/css2?family=Open+Sans:wght@400;700&display=swap">
<style>
  :root {
    --page-bg: #3b3532;
    --card-black: #050505;
    --card-sheen: #1c1c20;
    --royal-blue: #2f3590;
    --platinum: #e6e6e6;
    --silver: #aaaaaa;
    --text-white: #ffffff;
  }
  * { margin: 0; padding: 0; box-sizing: border-box; }
  html, body {
    width: 1200px;
    height: 844px;
    overflow: hidden;
    background: var(--page-bg);
    font-family: "Open Sans", Arial, sans-serif;
  }
  .canvas {
    position: relative;
    width: 1200px;
    height: 844px;
  }
  .card {
    position: absolute;
    top: 272px;
    width: 525px;
    height: 300px;
    background: var(--card-black);
    overflow: hidden;
    box-shadow: 0 10px 24px rgba(0, 0, 0, 0.45);
  }

  /* Contact side */
  .card--contact { left: 50px; }
  .card--contact::before {
    content: "";
    position: absolute;
    inset: 0;
    background: radial-gradient(ellipse at 35% 65%, var(--card-sheen) 0%, var(--card-black) 60%);
  }
  .band {
    position: absolute;
    left: 0;
    width: 100%;
    height: 14px;
    background: var(--royal-blue);
  }
  .band--top { top: 0; }
  .band--bottom { bottom: 0; }
  .contact-block {
    position: absolute;
    left: 210px;
    top: 56px;
    width: 260px;
    text-align: center;
    color: var(--text-white);
  }
  .contact-name {
    font-size: 17px;
    font-weight: 700;
    line-height: 1.2;
  }
  .contact-title {
    font-size: 12px;
    margin-bottom: 24px;
  }
  .contact-lines {
    list-style: none;
    font-size: 12.5px;
    line-height: 1.55;
  }
  .contact-address {
    margin-top: 30px;
    font-size: 12.5px;
    white-space: nowrap;
  }

  /* Brand side */
  .card--brand {
    left: 625px;
    background: radial-gradient(ellipse at 50% 40%, #26262a 0%, var(--card-black) 65%);
  }
  .edge-tab {
    position: absolute;
    width: 34px;
    height: 22px;
    background: linear-gradient(to right, var(--royal-blue) 0 70%, var(--platinum) 70% 82%, var(--royal-blue) 82% 100%);
  }
  .edge-tab--top { top: 0; right: 50px; }
  .edge-tab--left { left: 0; top: 212px; }
  .brand-name {
    position: absolute;
    inset: 0;
    display: flex;
    align-items: center;
    justify-content: center;
    gap: 12px;
    color: var(--royal-blue);
    font-size: 34px;
    font-weight: 700;
    letter-spacing: 3px;
  }
  .brand-mark {
    width: 14px;
    height: 14px;
    border-radius: 50%;
    background: var(--royal-blue);
  }
</style>
</head>
<body>
  <main class="canvas">
    <section class="card card--contact" aria-label="Business card contact side">
      <div class="band band--top"></div>
      <div class="contact-block">
        <p class="contact-name">Laura Bennett</p>
        <p class="contact-title">Principal</p>
        <ul class="contact-lines">
          <li>T: 555.208.3170</li>
          <li>E: lbennett@solacetravel.com</li>
          <li>W: solacetravel.com</li>
        </ul>
        <p class="contact-address">12 Harbour Lane, Lakeview, QC H0H 1A1</p>
      </div>
      <div class="band band--bottom"></div>
    </section>

    <section class="card card--brand" aria-label="Business card brand side">
      <div class="edge-tab edge-tab--top"></div>
      <div class="edge-tab edge-tab--left"></div>
      <div class="brand-name">
        <span class="brand-mark"></span>
        <span>Solace Travel</span>
      </div>
    </section>
  </main>
</body>
</html>
```